Corporate Business Card

Very professional, Modern, Not to busy, include phone address email, website
(253) 555-0174, 61807 19th Street N, Kent, WA 98517, marcus@kestrelbayholding.com, brelvanindustries.com

Target Market(s)

Manufacturing

Industry/Entity Type

Aero, machining, manufacturing, Off road racing

Contact Information for Business Card

Phone, address email, website

```html
<!DOCTYPE html>
<html lang="en">
<head>
<meta charset="utf-8">
<title>Brelvan Industries – Business Card</title>
<link rel="stylesheet" href="https://fonts.googleapis.com/css2?family=Open+Sans:wght@400;600;700&display=swap">
<style>
  :root {
    --navy: #1b3c8c;
    --navy-deep: #163275;
    --red: #d5333d;
    --ink: #4a4a4a;
    --paper: #ffffff;
    --stage: #2a2c30;
  }
  * { box-sizing: border-box; margin: 0; padding: 0; }
  html, body {
    width: 1200px; height: 900px; overflow: hidden;
    background: var(--stage);
    font-family: "Open Sans", Arial, sans-serif;
  }
  .stage {
    width: 1200px; height: 900px;
    display: flex; align-items: center; justify-content: center; gap: 48px;
  }
  .card {
    width: 532px; height: 304px; position: relative; overflow: hidden;
    border-radius: 3px;
    box-shadow: 0 10px 28px rgba(0,0,0,.45);
  }

  /* Front */
  .card--front { background: var(--paper); }
  .holder { position: absolute; left: 34px; top: 36px; }
  .holder__name { color: var(--navy); font-weight: 700; font-size: 25px; line-height: 1.1; }
  .holder__title { color: var(--ink); font-size: 12px; margin-top: 3px; }
  .brand {
    position: absolute; right: 34px; top: 40px; text-align: right;
  }
  .brand__name {
    color: var(--navy); font-weight: 700; font-size: 26px; line-height: 1.1;
    display: flex; align-items: center; gap: 8px; justify-content: flex-end;
  }
  .brand__mark { width: 12px; height: 12px; background: var(--red); display: inline-block; }
  .brand__rule { display: block; width: 150px; height: 1px; background: var(--navy); margin: 10px 0 0 auto; }
  .divider {
    position: absolute; left: 34px; right: 34px; top: 126px; height: 1px; background: var(--navy);
  }
  .contacts { position: absolute; left: 34px; top: 140px; list-style: none; }
  .contacts li {
    display: flex; align-items: center; gap: 8px;
    color: var(--ink); font-size: 12.5px; line-height: 21px;
  }
  .contacts svg { width: 11px; height: 11px; flex: none; }
  .address {
    position: absolute; right: 34px; bottom: 30px; text-align: right;
    color: var(--ink); font-size: 14px; line-height: 1.4; font-style: normal;
  }

  /* Back */
  .card--back {
    background: linear-gradient(135deg, var(--navy) 0%, var(--navy-deep) 100%);
    display: flex; align-items: center; justify-content: center;
  }
  .world-map {
    position: absolute; left: 40px; top: 20px; right: 40px; bottom: 20px;
    background: radial-gradient(ellipse at 50% 50%, rgba(255,255,255,.10) 0%, rgba(255,255,255,0) 70%);
  }
  .back-brand { position: relative; text-align: center; }
  .back-brand__name {
    color: var(--paper); font-weight: 700; font-size: 34px;
    display: flex; align-items: center; gap: 10px;
  }
  .back-brand__mark { width: 14px; height: 14px; background: var(--red); display: inline-block; }
  .back-brand__rule { display: block; width: 170px; height: 1px; background: rgba(255,255,255,.8); margin: 12px auto 0 0; }
</style>
</head>
<body>
<main class="stage">
  <section class="card card--front" aria-label="Business card front">
    <header class="holder">
      <h1 class="holder__name">Daniel Whitford</h1>
      <p class="holder__title">President and CEO</p>
    </header>
    <div class="brand">
      <div class="brand__name"><span class="brand__mark"></span>Brelvan Industries</div>
      <span class="brand__rule"></span>
    </div>
    <span class="divider"></span>
    <ul class="contacts">
      <li>
        <svg viewBox="0 0 12 12" aria-hidden="true"><path fill="var(--red)" d="M2.5 1l2 2-1 1.5c.6 1.4 1.6 2.4 3 3L8 6.5l2 2-1.2 1.7C5 10 2 7 1.8 3.2z"/></svg>
        (253) 555-0174
      </li>
      <li>
        <svg viewBox="0 0 12 12" aria-hidden="true"><rect x="1" y="2.5" width="10" height="7" rx="1" fill="var(--red)"/><path d="M1.5 3l4.5 3.5L10.5 3" stroke="#fff" fill="none" stroke-width="1"/></svg>
        marcus@kestrelbayholding.com
      </li>
      <li>
        <svg viewBox="0 0 12 12" aria-hidden="true"><circle cx="6" cy="6" r="5" fill="var(--red)"/><path d="M1 6h10M6 1c2 2.5 2 7.5 0 10M6 1c-2 2.5-2 7.5 0 10" stroke="#fff" fill="none" stroke-width=".8"/></svg>
        brelvanindustries.com
      </li>
    </ul>
    <address class="address">61807 19th Street N<br>Kent, WA 98517</address>
  </section>

  <section class="card card--back" aria-label="Business card back">
    <div class="world-map" role="img" aria-label="Faint dotted world map"></div>
    <div class="back-brand">
      <div class="back-brand__name"><span class="back-brand__mark"></span>Brelvan Industries</div>
      <span class="back-brand__rule"></span>
    </div>
  </section>
</main>
</body>
</html>
```